Agricultural Commodities Specialist Needs a Business Card Design

Business owner Rob Hartwell, need a business card design for his company based in Brisbane, Australia called "RH Tradelink Pty Ltd".
Rob is an Agricultural Commodities Specialist:
-Specialising in Domestic and Export of Cotton,Cottonseed and Grains.
-Extensive experience in exporting into Asia especially China.
-Buyers agent for one of China's largest spinning mills.
-Capital raising from foreign investors into Australian agriculture.
-Agricultural marketing strategies for corporate and family farms.
-Importer of niche products from China.
-Array of contacts in agriculture and manufacturing in China.

Rob would like a professional business card with his company name "RH Tradelink" on the front of his business card - with contact details on the back. Preferably black and white colours.

CONTACT DETAILS THAT NEED TO BE INCLUDED:

Rob Hartwell
Mobile: 0431 275 604

Po Box 518
Elm Vale QLD 4187

Email: rob@rhtradelinkco.com
website: www.rhtradelinkc.com

```html
<!DOCTYPE html>
<html lang="en">
<head>
<meta charset="utf-8">
<title>RH Tradelink – Business Card</title>
<link rel="stylesheet" href="https://fonts.googleapis.com/css2?family=Cinzel:wght@400;500&family=Open+Sans:wght@400&display=swap">
<style>
  :root {
    --page-bg: #eeeeec;
    --card-bg: #ffffff;
    --card-edge: #4a4a4a;
    --brand-blue: #1d4f8c;
    --brand-green: #6ab42d;
    --ink: #2b2b2b;
    --ink-soft: #3c3c3c;
  }
  * { box-sizing: border-box; margin: 0; padding: 0; }
  html, body { width: 949px; height: 1200px; overflow: hidden; }
  body {
    background: var(--page-bg);
    position: relative;
    font-family: "Open Sans", Arial, sans-serif;
    color: var(--ink);
  }
  .card {
    position: absolute;
    left: 102px;
    width: 745px;
    height: 426px;
    background: radial-gradient(ellipse at 50% 40%, #ffffff 55%, #f1f1f1 100%);
    border: 1px solid var(--card-edge);
  }
  .card--front { top: 71px; }
  .card--back { top: 621px; }

  /* front */
  .brand-name {
    position: absolute;
    font-family: "Cinzel", Georgia, serif;
    font-weight: 400;
    color: var(--brand-blue);
    white-space: nowrap;
  }
  .card--front .brand-name {
    top: 110px;
    left: 0;
    width: 726px;
    text-align: center;
    font-size: 44px;
    letter-spacing: 1px;
  }
  .divider {
    position: absolute;
    left: 363px;
    top: 248px;
    width: 1.5px;
    height: 142px;
    background: linear-gradient(to bottom, transparent, var(--brand-blue) 30%, var(--brand-blue) 70%, transparent);
  }
  .holder {
    position: absolute;
    right: 395px;
    top: 262px;
    text-align: right;
    font-family: "Cinzel", Georgia, serif;
    font-size: 20px;
    line-height: 25px;
    color: var(--ink);
  }
  .holder__name { color: var(--brand-green); }
  .contact-list {
    position: absolute;
    left: 391px;
    top: 262px;
    list-style: none;
    font-family: "Cinzel", Georgia, serif;
    font-size: 18.5px;
    line-height: 25px;
    color: var(--ink);
  }
  .contact-list li { display: flex; align-items: center; gap: 8px; }
  .contact-list svg { width: 15px; height: 15px; flex: none; }

  /* back */
  .card--back .brand-mark {
    position: absolute;
    left: 42px;
    top: 212px;
    display: flex;
    align-items: center;
    gap: 12px;
  }
  .brand-square {
    width: 26px;
    height: 26px;
    background: var(--brand-green);
  }
  .card--back .brand-name {
    position: static;
    font-size: 29px;
  }
  .services {
    position: absolute;
    left: 364px;
    top: 74px;
    list-style: none;
    font-size: 14.6px;
    line-height: 17.8px;
    color: var(--ink-soft);
  }
  .services li {
    position: relative;
    padding-left: 21px;
    margin-bottom: 0;
  }
  .services li::before {
    content: "";
    position: absolute;
    left: 0;
    top: 1px;
    width: 15px;
    height: 15px;
    border-radius: 50%;
    background: radial-gradient(circle at 35% 35%, #9bd75c, var(--brand-green) 60%, #4f8f1e);
  }
  .web-line {
    position: absolute;
    right: 17px;
    top: 364px;
    font-family: "Cinzel", Georgia, serif;
    font-size: 16px;
    letter-spacing: 5.2px;
    color: var(--ink);
  }
</style>
</head>
<body>

<section class="card card--front" aria-label="Business card front">
  <div class="brand-name">RH Tradelink</div>
  <div class="divider"></div>
  <div class="holder">
    <div class="holder__name">Rob Hartwell</div>
    <div>Po Box 518</div>
    <div>Elm Vale QLD 4187</div>
  </div>
  <ul class="contact-list">
    <li>
      <svg viewBox="0 0 16 16" aria-hidden="true"><circle cx="8" cy="8" r="8" fill="#6ab42d"/><rect x="5.2" y="3.5" width="5.6" height="9" rx="1" fill="#fff"/><rect x="6.2" y="4.6" width="3.6" height="5" fill="#6ab42d"/></svg>
      0431 275 604
    </li>
    <li>
      <svg viewBox="0 0 16 16" aria-hidden="true"><circle cx="8" cy="8" r="8" fill="#6ab42d"/><rect x="3.8" y="5" width="8.4" height="6" fill="#fff"/><path d="M3.8 5 L8 8.4 L12.2 5" fill="none" stroke="#6ab42d" stroke-width="1"/></svg>
      rob@rhtradelinkco.com
    </li>
    <li>
      <svg viewBox="0 0 16 16" aria-hidden="true"><circle cx="8" cy="8" r="8" fill="#6ab42d"/><circle cx="8" cy="8" r="4.6" fill="none" stroke="#fff" stroke-width="1"/><ellipse cx="8" cy="8" rx="2" ry="4.6" fill="none" stroke="#fff" stroke-width="1"/><path d="M3.4 8 H12.6" stroke="#fff" stroke-width="1"/></svg>
      www.rhtradelinkc.com
    </li>
  </ul>
</section>

<section class="card card--back" aria-label="Business card back">
  <div class="brand-mark">
    <span class="brand-square"></span>
    <span class="brand-name">RH Tradelink</span>
  </div>
  <ul class="services">
    <li>Specialising in Domestic and Export<br>of Cotton,Cottonseed and Grains.</li>
    <li>Extensive experience in exporting<br>into Asia especially China.</li>
    <li>Buyers agent for one of China's<br>largest spinning mills.</li>
    <li>Capital raising from foreign investors<br>into Australian agriculture.</li>
    <li>Agricultural marketing strategies for<br>corporate and family farms.</li>
    <li>Importer of niche products from China.</li>
    <li>Array of contacts in agriculture and<br>manufacturing in China</li>
  </ul>
  <div class="web-line">WWW.RHTRADELINKC.COM</div>
</section>

</body>
</html>
```